Folding Marigold Book Cover

Book cover for both print paperback and ebook versions of a collection of short stories. Publisher is Quiet Harbor Publishers. The cover needs to capture the essence of the title concept to be chosen. Print cover template is attached as well as logo file. The book title is "Folding Marigold, Short Stories by Ross T. Perevy"

The concept is related to the movie Velvet Crank, where character Barney Quellwood explains his amps are louder because they go to eleven. If you are not familiar, go to vidmorrow and search for "Velvet Crank, eleven" to see the scene. The concept can also be explained as a person who persists in a belief or behavior in spite of overwhelming evidence it makes little sense.

Target Market(s)

Adult fiction, short stories,

Font styles to use
Serif

Colors

Designer to choose colors to be used in the design.

Requirements
Must have
• Must be more than the obvious amp dial, showing it goes to eleven. It should be a creative take on the concept.
Nice to have
• Possible Ideas;
• - person betting all-in on an inside straight (cards showing, pushing chips forward..)
• - some creative play on the amp dials
Should not have
• Do not provide artwork with elements we have to arrange for an extra license. AI compatible files only.

```html
<!DOCTYPE html>
<html lang="en">
<head>
<meta charset="utf-8">
<title>Folding Marigold – Cover Spread</title>
<link rel="stylesheet" href="https://fonts.googleapis.com/css2?family=Oswald:wght@500&family=EB+Garamond:wght@400;500&display=swap">
<style>
  :root {
    --backdrop: #e1e1e1;
    --paper: #ffffff;
    --spine-shade: #f1f1f1;
    --title-red: #e3111e;
    --ink: #1d1d1d;
    --smoke-light: #f4f5f8;
    --smoke-mid: #9aa0a8;
    --stage-dark: #0c0d0f;
    --logo-green: #1f5a36;
    --author-light: #f2f2f2;
  }
  * { box-sizing: border-box; margin: 0; padding: 0; }
  html, body {
    width: 1200px; height: 800px; overflow: hidden;
    background: var(--backdrop);
  }
  .cover-spread {
    position: absolute; left: 110px; top: 60px;
    width: 980px; height: 680px;
    display: flex;
    box-shadow: 0 18px 40px rgba(0,0,0,0.18);
  }
  /* Back cover */
  .back-cover {
    width: 450px; height: 100%;
    background: var(--paper);
    padding: 62px 50px 34px;
    display: flex; flex-direction: column;
  }
  .back-cover__title {
    font-family: "Oswald", sans-serif; font-weight: 500;
    color: var(--title-red); font-size: 38px; line-height: 1;
    text-align: center; letter-spacing: 0.5px;
  }
  .back-cover__byline {
    font-family: "EB Garamond", serif; font-size: 16px;
    letter-spacing: 4px; text-align: center; color: var(--ink);
    margin-top: 8px;
  }
  .back-cover__blurb {
    font-family: "EB Garamond", serif; font-size: 13.5px; line-height: 1.3;
    color: var(--ink);
  }
  .back-cover__blurb--first { margin: 40px 20px 0 30px; }
  .back-cover__blurb--second { margin: 40px 0 0 70px; }
  .publisher-mark {
    display: flex; align-items: center; gap: 6px;
    font-family: "EB Garamond", serif; font-size: 11px; color: var(--ink);
    line-height: 1.1;
  }
  .publisher-mark__square {
    width: 26px; height: 26px; background: var(--logo-green); flex: none;
  }
  .back-cover .publisher-mark {
    margin-top: auto; align-self: center; width: 110px;
  }
  /* Spine */
  .spine {
    width: 80px; height: 100%;
    background: linear-gradient(90deg, var(--spine-shade), var(--paper) 30%, var(--paper) 70%, var(--spine-shade));
    display: flex; flex-direction: column; align-items: center;
    padding: 36px 0 24px;
  }
  .spine__title {
    writing-mode: vertical-rl;
    font-family: "Oswald", sans-serif; font-weight: 500;
    color: var(--title-red); font-size: 32px; letter-spacing: 0.5px;
  }
  .spine__author {
    writing-mode: vertical-rl;
    font-family: "EB Garamond", serif; font-size: 16px; letter-spacing: 3px;
    color: var(--ink); margin-top: 70px;
  }
  .spine .publisher-mark {
    margin-top: auto;
    flex-direction: column; gap: 3px; text-align: center; font-size: 9px;
    width: 70px;
  }
  /* Front cover */
  .front-cover {
    width: 450px; height: 100%;
    position: relative; overflow: hidden;
  }
  .front-cover__photo {
    position: absolute; inset: 0;
    background:
      radial-gradient(ellipse 60% 45% at 45% 32%, var(--smoke-light) 0%, rgba(220,224,230,0.85) 40%, rgba(154,160,168,0) 80%),
      linear-gradient(180deg, #5c6068 0%, var(--smoke-mid) 30%, #6e737b 55%, #25272b 78%, var(--stage-dark) 100%);
  }
  .front-cover__title {
    position: absolute; left: 70px; top: 140px;
    font-family: "Oswald", sans-serif; font-weight: 500;
    color: var(--title-red); font-size: 76px; line-height: 1.02;
    letter-spacing: 1px;
  }
  .front-cover__author {
    position: absolute; left: 0; right: 0; bottom: 40px; text-align: center;
    font-family: "EB Garamond", serif; font-size: 30px; letter-spacing: 7px;
    color: var(--author-light);
  }
</style>
</head>
<body>
  <main class="cover-spread">
    <section class="back-cover">
      <h2 class="back-cover__title">FOLDING MARIGOLD</h2>
      <p class="back-cover__byline">BY ROSS T. PEREVY</p>
      <p class="back-cover__blurb back-cover__blurb--first">Lorem ipsum dolor sit amet, consectetur adipiscing elit, sed do eiusmod tempor incididunt ut labore et dolore magna aliqua. Nunc congue nisi vitae suscipit tellus mauris a diam maecenas. Enim lobortis scelerisque fermentum dui faucibus in ornare quam viverra. Malesuada bibendum arcu vitae elementum curabitur. Viverra suspendisse potenti nullam ac tortor vitae. Sed felis eget velit aliquet sagittis id consectetur purus. Nullam non nisi est sit amet facilisis magna etiam. Metus aliquam eleifend mi in nulla posuere sollicitudin aliquam. Habitasse platea dictumst quisque sagittis purus sit. Malesuada proin</p>
      <p class="back-cover__blurb back-cover__blurb--second">Augue eget arcu dictum varius duis at. Ullamcorper eget nulla facilisi etiam dignissim diam quis. Vitae aliquet nec ullamcorper sit amet risus nullam. Pulvinar neque laoreet suspendisse interdum consectetur libero id faucibus. Gravida dictum fusce ut placerat orci nulla pellentesque dignissim enim. Nibh tellus molestie nunc non blandit massa enim nec dui. Ultrices eros in cursus turpis massa tincidunt.</p>
      <div class="publisher-mark">
        <span class="publisher-mark__square"></span>
        <span>Quiet Harbor Publishers</span>
      </div>
    </section>

    <section class="spine">
      <span class="spine__title">FOLDING MARIGOLD</span>
      <span class="spine__author">ROSS T. PEREVY</span>
      <div class="publisher-mark">
        <span class="publisher-mark__square"></span>
        <span>Quiet Harbor Publishers</span>
      </div>
    </section>

    <section class="front-cover">
      <div class="front-cover__photo" role="img" aria-label="Black-and-white photo of a guitarist seen from behind on a smoky stage beside a stack of amplifiers"></div>
      <h1 class="front-cover__title">FOLDING<br>MARIGOLD</h1>
      <p class="front-cover__author">ROSS T. PEREVY</p>
    </section>
  </main>
</body>
</html>
```